Brightwave Limber Health Clinic logo design

At the Brightwave Limber Health Clinic, we are committed to relieving any soft tissue related pain or injury by offering premium health care consultations and hands on therapy services. It is our intention to promote and support healthy living and well being within the local community.

The services available at Brightwave Limber will include remedial, therapeutic, sports, pregnancy and relaxation massage. At Brightwave Limber we also sell products that will assist in rehabilitation, strengthening and maintaining muscle suppleness and correct posture.

We would like to see the funky logo design be displayed on a businesiness card.

The colors we would like to be used or incorporated on the business card are browns(can't be background colour unless very light) and greens - because we will be writing appointment times at the back of the cards

The final design should communicate: freedom in body movement, have a community feel if possible.

We are open to the use of appropriate graphics

We would like to use the back of the card to write down client's next scheduled appointments. Allow 4 or 5 lines below the heading Next Scheduled Appointment Time. Please communicate at the back that
- Late Arrival may reduce treatment time
-24 hour cancellation notice is required or a cancellation fee is incurred
Updates

Project Deadline Extended
Reason: Haven't been happy with the designs submitted

Target Market(s)

Target market would incluce yummy mummies/soccer mums, weekend atheletes and the suites

Industry/Entity Type

Health

Logo Text

Logo styles of interest
Emblem Logo
Pictorial/Combination Logo
Abstract Logo
Lettermark Logo
Requirements
Must have
• At the front of the Business Card, the following details needs to be printed:

Mira Lo
Remedial Massage Therapist
Dip REM, BBus(Mktg), Member of KPRC Association

M: 0491 657 408
Nice to have
• It would be nice to have a logo thats energetic, vibrant, something that will stand out

```html
<!DOCTYPE html>
<html lang="en">
<head>
<meta charset="utf-8">
<title>Brightwave Limber Health Clinic – Business Card</title>
<link rel="stylesheet" href="https://fonts.googleapis.com/css2?family=Heebo:wght@200;300;500&display=swap">
<style>
  :root {
    --paper: #ffffff;
    --card-yellow: #e3e176;
    --olive: #b3b04a;
    --olive-soft: #cfcc62;
    --brown: #4f421c;
    --cloud-light: #f6f5cf;
    --cloud-mid: #f0eeb2;
    --rule: #e4e2b8;
  }
  * { margin: 0; padding: 0; box-sizing: border-box; }
  html, body { width: 848px; height: 1200px; overflow: hidden; background: var(--paper); }
  body { position: relative; font-family: "Heebo", "Helvetica Neue", Arial, sans-serif; color: var(--brown); }

  .card { position: absolute; left: 212px; width: 365px; height: 224px; overflow: hidden; }
  .card--front { top: 333px; background: var(--card-yellow); }
  .card--back { top: 680px; background: var(--paper); border: 1px solid var(--rule); border-top: none; }

  .hand-art {
    position: absolute;
    background: linear-gradient(135deg, rgba(200,197,90,0.35), rgba(227,225,118,0));
    border-radius: 40% 50% 30% 10%;
  }
  .card--front .hand-art { left: 0; top: 14px; width: 178px; height: 198px; }

  .therapist { position: absolute; left: 222px; top: 18px; }
  .therapist__name { font-size: 17px; font-weight: 200; font-style: italic; letter-spacing: -0.3px; }
  .therapist__details { margin-top: 6px; font-size: 7.6px; font-weight: 500; line-height: 10.5px; letter-spacing: -0.2px; }
  .therapist__phone { margin-top: 6px; font-size: 7.6px; font-weight: 300; color: var(--cloud-light); letter-spacing: 0.3px; }

  .clinic-name {
    position: absolute; font-weight: 200; color: var(--olive); letter-spacing: -0.5px; line-height: 1;
  }
  .card--front .clinic-name { left: 58px; top: 118px; font-size: 32px; }
  .clinic-tagline { position: absolute; font-weight: 300; color: var(--brown); white-space: nowrap; }
  .card--front .clinic-tagline { left: 86px; top: 162px; font-size: 10.5px; }

  .back-band { position: absolute; left: 0; top: 0; width: 100%; height: 152px; background: var(--card-yellow); }
  .card--back .hand-art { left: 0; top: 6px; width: 62px; height: 80px; }
  .card--back .clinic-name { left: 34px; top: 48px; font-size: 14px; }
  .card--back .clinic-tagline { left: 36px; top: 65px; font-size: 4.5px; }

  .services { position: absolute; right: 4px; top: 2px; text-align: right; font-weight: 200; line-height: 0.86; letter-spacing: -0.4px; }
  .services span { display: block; }
  .s-remedial { font-size: 18px; color: var(--cloud-light); }
  .s-therapeutic { font-size: 17px; color: var(--cloud-mid); font-style: italic; }
  .s-sports { font-size: 15px; color: var(--paper); margin-right: 40px; }
  .s-pregnancy { font-size: 17px; color: var(--cloud-mid); font-style: italic; }
  .s-relaxing { font-size: 16px; color: var(--paper); }
  .s-rehab { font-size: 11px; color: var(--olive-soft); margin-right: 18px; }
  .s-strength { font-size: 14px; color: var(--paper); margin-right: 16px; }
  .s-maintain { font-size: 13px; color: var(--cloud-mid); font-style: italic; margin-right: 14px; }
  .s-muscle { font-size: 14px; color: var(--cloud-light); margin-right: 12px; }
  .s-supple { font-size: 10px; color: var(--olive-soft); margin-right: 26px; }
  .s-correct { font-size: 14px; color: var(--cloud-light); margin-right: 18px; }
  .s-posture { font-size: 18px; color: var(--cloud-mid); font-style: italic; margin-right: 22px; }

  .appointments { position: absolute; left: 36px; top: 134px; font-size: 14px; font-weight: 200; font-style: italic; letter-spacing: -0.3px; color: var(--brown); }
  .appointment-line { position: absolute; left: 36px; top: 195px; width: 196px; height: 1px; background: var(--rule); }
</style>
</head>
<body>
  <section class="card card--front" aria-label="Business card front">
    <div class="hand-art" role="img" aria-label="Line drawing of a hand making an OK gesture"></div>
    <div class="clinic-name">Brightwave Limber</div>
    <div class="clinic-tagline">brightwave limber health clinic</div>
    <div class="therapist">
      <div class="therapist__name">Mira Lo</div>
      <div class="therapist__details">Remedial Massage Therapist<br>Dip REM, BBus(Mktg),<br>Member of KPRC Association</div>
      <div class="therapist__phone">M: 0491 657 408</div>
    </div>
  </section>

  <section class="card card--back" aria-label="Business card back">
    <div class="back-band"></div>
    <div class="hand-art" role="img" aria-label="Small line drawing of a hand making an OK gesture"></div>
    <div class="clinic-name">Brightwave Limber</div>
    <div class="clinic-tagline">brightwave limber health clinic</div>
    <div class="services">
      <span class="s-remedial">remedial</span>
      <span class="s-therapeutic">therapeutic</span>
      <span class="s-sports">sports</span>
      <span class="s-pregnancy">pregnancy</span>
      <span class="s-relaxing">relaxing</span>
      <span class="s-rehab">rehabilitation</span>
      <span class="s-strength">strengthening</span>
      <span class="s-maintain">maintaining</span>
      <span class="s-muscle">muscle</span>
      <span class="s-supple">suppleness</span>
      <span class="s-correct">correct</span>
      <span class="s-posture">posture</span>
    </div>
    <div class="appointments">APPOINTMENTS:</div>
    <div class="appointment-line"></div>
  </section>
</body>
</html>
```